Retractable Banner Stands

Hello we need a deisgn for a banner.
Sizes: 36"x80", 12"x17"(this one to have less on it, most the logo, license numvber, and address), and a 24"x40" banner
Roofing Services
HOA & Commercial Roofing
• Emergency roof tarping & repairs — Starting at $550
• Small & large roof repairs
• Preventative roof maintenance
• Full roof replacement
Deck & Balcony Services
• Balcony & deck maintenance
SB-326 Repairs
• Deck resurfacing
• Small & large deck repairs
• Full deck reconstruction
Gutter Services
• Small & large gutter repairs
• Gutter cleaning & maintenance
• New gutter installation & replacement
License Information:
C-39 Roofing Contractor
General B Contractor
License #4529730
📍 Serving Orange County & Surrounding Areas
📍 Office Location:
41 Dunwick Street, Suite F
Target Market(s)
HOA & Commerical roofs
Industry/Entity Type
Roofing
Other font styles liked:
- Gotham
Look and feel

```html
<!DOCTYPE html>
<html lang="en">
<head>
<meta charset="utf-8">
<title>Crestline Roofing & Waterproofing – Roll-up Banner</title>
<link href="https://fonts.googleapis.com/css2?family=Montserrat:wght@600;700;800&family=Catamaran:wght@500;600;700&display=swap" rel="stylesheet">
<style>
  :root{
    --stage:#9c9c9c;
    --sky-deep:#0a6cc0;
    --sky:#2f9fe6;
    --sky-light:#8fd0f7;
    --mist:#ffffff;
    --accent:#29a8e8;
    --ink:#1d1d1f;
    --sand:#ecd5b0;
    --roof:#4d5660;
  }
  *{margin:0;padding:0;box-sizing:border-box}
  html,body{width:1200px;height:1117px;overflow:hidden;background:var(--stage)}
  .banner{
    position:absolute;left:380px;top:18px;width:440px;height:1080px;overflow:hidden;
    background:
      radial-gradient(ellipse 62% 40% at 50% 58%, var(--mist) 40%, rgba(255,255,255,0) 100%),
      linear-gradient(180deg,var(--sky-deep) 0%,var(--sky) 22%,var(--sky-light) 50%,#d8effc 72%,var(--mist) 78%);
    font-family:"Catamaran",sans-serif;color:var(--ink);
  }
  .brand{position:absolute;top:58px;left:0;width:100%;text-align:center;color:#fff;font-family:"Montserrat",sans-serif}
  .brand-name{font-weight:800;font-size:56px;letter-spacing:1px;line-height:1;display:inline-flex;align-items:center;gap:10px}
  .brand-mark{width:14px;height:14px;background:#fff;display:inline-block}
  .brand-tag{margin-top:44px;font-weight:600;font-size:20px;letter-spacing:.5px}
  .headline{position:absolute;top:196px;width:100%;text-align:center;color:#fff;font-family:"Montserrat",sans-serif;font-weight:800;font-size:64px;line-height:1;letter-spacing:-1px;text-shadow:0 3px 8px rgba(0,60,120,.35)}
  .subhead-band{position:absolute;top:290px;left:60px;width:320px;height:58px;background:linear-gradient(90deg,rgba(41,168,232,0),var(--accent) 20%,var(--accent) 80%,rgba(41,168,232,0))}
  .subhead{position:absolute;top:296px;width:100%;text-align:center;color:#fff;font-family:"Montserrat",sans-serif;font-weight:800;font-size:46px;line-height:1;letter-spacing:-1px}
  .service{position:absolute;left:48px;width:360px;display:flex;gap:14px}
  .service svg{flex:none;width:40px;height:66px}
  .service h2{font-family:"Montserrat",sans-serif;font-weight:700;font-size:18px;color:var(--accent);letter-spacing:-.3px;margin:4px 0 8px}
  .service ul{list-style:none}
  .service li{position:relative;padding-left:26px;font-size:12.5px;font-weight:600;line-height:1.3;margin-bottom:9px}
  .service li::before{content:"";position:absolute;left:0;top:3px;border-left:8px solid var(--accent);border-top:5px solid transparent;border-bottom:5px solid transparent}
  .svc-hoa{top:358px}.svc-deck{top:518px}.svc-gutter{top:664px}
  .roof-photo{position:absolute;left:0;top:800px;width:100%;height:170px;
    background:linear-gradient(180deg,rgba(255,255,255,0) 0%,#c9e4f5 30%,var(--roof) 58%,#3a424a 100%)}
  .footer{position:absolute;left:0;top:965px;width:100%;height:115px;background:var(--sand)}
  .area-strip{position:absolute;left:26px;top:986px;width:372px;height:26px;background:var(--accent);color:#fff;font-family:"Montserrat",sans-serif;font-weight:700;font-size:12.5px;line-height:26px;text-align:center}
  .office{position:absolute;left:38px;top:1018px;display:flex;gap:14px;align-items:flex-start}
  .office svg{width:36px;height:40px;margin-top:4px}
  .office-label{font-family:"Montserrat",sans-serif;font-weight:600;font-size:14px;line-height:1.1}
  .office-address{font-family:"Montserrat",sans-serif;font-weight:700;font-size:21px;line-height:1.3;letter-spacing:-.4px}
  .licenses{position:absolute;left:0;top:1058px;width:100%;text-align:center;font-size:11.5px;font-weight:500;color:#444}
  .licenses span+span{border-left:1px solid var(--accent);margin-left:10px;padding-left:10px}
</style>
</head>
<body>
<main class="banner">
  <header class="brand">
    <div class="brand-name">CRESTLINE<span class="brand-mark"></span></div>
    <div class="brand-tag">ROOFING &amp; WATERPROOFING</div>
  </header>

  <h1 class="headline">ROOFING</h1>
  <div class="subhead-band"></div>
  <div class="subhead">SERVICES</div>

  <section class="service svc-hoa">
    <svg viewBox="0 0 40 66"><path d="M20 2 C28 20 38 32 38 46 A18 18 0 0 1 2 46 C2 32 12 20 20 2Z" fill="var(--accent)"/></svg>
    <div>
      <h2>HOA &amp; COMMERCIAL ROOFING</h2>
      <ul>
        <li>Emergency roof tarping &amp; repairs –<br>Starting at $550</li>
        <li>Small &amp; large roof repairs</li>
        <li>Preventative roof maintenance</li>
        <li>Full roof replacement</li>
      </ul>
    </div>
  </section>

  <section class="service svc-deck">
    <svg viewBox="0 0 40 66"><path d="M20 2 C28 20 38 32 38 46 A18 18 0 0 1 2 46 C2 32 12 20 20 2Z" fill="var(--accent)"/></svg>
    <div>
      <h2>DECK &amp; BALCONY SERVICES</h2>
      <ul>
        <li>Balcony &amp; deck maintenance SB-326 Repairs</li>
        <li>Deck resurfacing</li>
        <li>Small &amp; large deck repairs</li>
        <li>Full deck reconstruction</li>
      </ul>
    </div>
  </section>

  <section class="service svc-gutter">
    <svg viewBox="0 0 40 66"><path d="M20 2 C28 20 38 32 38 46 A18 18 0 0 1 2 46 C2 32 12 20 20 2Z" fill="var(--accent)"/></svg>
    <div>
      <h2>GUTTER SERVICES</h2>
      <ul>
        <li>Small &amp; large gutter repairs</li>
        <li>Gutter cleaning &amp; maintenance</li>
        <li>New gutter installation &amp; replacement</li>
      </ul>
    </div>
  </section>

  <div class="roof-photo" role="img" aria-label="Photo of a tiled roof with a white-trimmed dormer window against a blue sky"></div>

  <footer class="footer"></footer>
  <div class="area-strip">SERVING ORANGE COUNTY &amp; SURROUNDING AREAS</div>
  <div class="office">
    <svg viewBox="0 0 36 40" aria-hidden="true">
      <ellipse cx="18" cy="33" rx="16" ry="5" fill="none" stroke="var(--accent)" stroke-width="2"/>
      <path d="M18 33 C12 24 8 19 8 13 A10 10 0 0 1 28 13 C28 19 24 24 18 33Z" fill="var(--accent)"/>
      <circle cx="18" cy="13" r="4" fill="var(--sand)"/>
    </svg>
    <div>
      <div class="office-label">Office Location:</div>
      <div class="office-address">41 Dunwick Street, Suite F</div>
    </div>
  </div>
  <div class="licenses"><span>C-39 Roofing Contractor</span><span>General B Contractor</span><span>License #4529730</span></div>
</main>
</body>
</html>
```